Business card for a yoga studio
The Reed Yoga Studio
Project: Business card for a yoga studio
Business card for a yoga studio - Health
Creative Brief
Bright & Fun-filled
Lorna Pichet
Owner
27316 Hollin Avenue, Suite 408 Dallas, TX 75219
972-318-YOGA(9642)
lorna@thereedyogastudio.example
TheReedYogaStudio.example
Would like a new/fresh business card design since we have moved. Don't like the dark/heavy feel of the existing card. I would like the phone number to appear as: 972-318-YOGA(9642).
TheReedYogaStudio TheReedYogaStudio
Would like to avoid solid black background or solid dark color background due to the way the cards show wear easily in everyday use/transport, as well as fingerprints.

```html
<!DOCTYPE html>
<html lang="en">
<head>
<meta charset="utf-8">
<title>The Reed Yoga Studio – Business Card</title>
<link rel="stylesheet" href="https://fonts.googleapis.com/css2?family=Open+Sans:wght@400;700&display=swap">
<style>
  :root {
    --backdrop: #f3f1ec;
    --card-edge: #cfe3d4;
    --card-edge-line: #a9cbb2;
    --card-face: #ffffff;
    --ink: #1e1e1e;
    --ink-soft: #4a4a4a;
    --rule: #c9c9c9;
    --icon: #2f6b4a;
  }
  html, body {
    margin: 0;
    width: 1200px;
    height: 900px;
    overflow: hidden;
    background: var(--backdrop);
    font-family: "Open Sans", Arial, sans-serif;
  }
  .canvas {
    position: relative;
    width: 1200px;
    height: 900px;
  }
  .card {
    position: absolute;
    left: 110px;
    top: 170px;
    width: 980px;
    height: 560px;
    background: var(--card-edge);
    border-radius: 14px;
    box-shadow: 0 10px 30px rgba(0, 0, 0, 0.08);
  }
  .card-face {
    position: absolute;
    inset: 26px;
    background: var(--card-face);
    border-radius: 44px;
    box-shadow: inset 0 0 0 3px var(--card-edge-line);
  }
  .brand {
    position: absolute;
    left: 30px;
    top: 250px;
    width: 340px;
    display: flex;
    align-items: center;
    justify-content: center;
    gap: 12px;
  }
  .brand-dot {
    width: 14px;
    height: 14px;
    border-radius: 50%;
    background: var(--icon);
    flex: none;
  }
  .brand-name {
    font-size: 26px;
    font-weight: 400;
    color: var(--ink);
    white-space: nowrap;
    line-height: 1.2;
  }
  .divider {
    position: absolute;
    left: 400px;
    top: 24px;
    bottom: 24px;
    width: 2px;
    background: var(--rule);
  }
  .person {
    position: absolute;
    left: 430px;
    top: 56px;
  }
  .person-name {
    margin: 0;
    font-size: 26px;
    font-weight: 700;
    color: var(--ink);
    line-height: 1.2;
  }
  .person-role {
    margin: 4px 0 0;
    font-size: 18px;
    color: var(--ink-soft);
  }
  .contact {
    position: absolute;
    left: 430px;
    top: 220px;
    margin: 0;
    padding: 0;
    list-style: none;
    font-size: 19px;
    color: var(--ink-soft);
  }
  .contact li {
    display: flex;
    align-items: flex-start;
    gap: 12px;
    margin-bottom: 12px;
    line-height: 1.4;
  }
  .contact svg {
    flex: none;
    width: 22px;
    height: 22px;
    margin-top: 3px;
  }
</style>
</head>
<body>
<main class="canvas">
  <section class="card" aria-label="The Reed Yoga Studio business card">
    <div class="card-face">
      <div class="brand">
        <span class="brand-dot"></span>
        <span class="brand-name">The Reed Yoga Studio</span>
      </div>
      <div class="divider"></div>
      <div class="person">
        <h1 class="person-name">Lorna Pichet</h1>
        <p class="person-role">Owner</p>
      </div>
      <ul class="contact">
        <li>
          <svg viewBox="0 0 22 22" aria-hidden="true"><circle cx="11" cy="11" r="11" fill="var(--icon)"/><path d="M11 5a4 4 0 0 0-4 4c0 3 4 8 4 8s4-5 4-8a4 4 0 0 0-4-4z" fill="#fff"/><circle cx="11" cy="9" r="1.5" fill="var(--icon)"/></svg>
          <span>27316 Hollin Avenue, Suite 408<br>Dallas, TX 75219</span>
        </li>
        <li>
          <svg viewBox="0 0 22 22" aria-hidden="true"><circle cx="11" cy="11" r="11" fill="var(--icon)"/><path d="M7.5 6h2l1 2.5-1.3 1a6 6 0 0 0 3.3 3.3l1-1.3 2.5 1v2a1 1 0 0 1-1 1A9 9 0 0 1 6.5 7a1 1 0 0 1 1-1z" fill="#fff"/></svg>
          <span>972-318-YOGA(9642)</span>
        </li>
        <li>
          <svg viewBox="0 0 22 22" aria-hidden="true"><circle cx="11" cy="11" r="11" fill="var(--icon)"/><rect x="5.5" y="7" width="11" height="8" rx="1" fill="#fff"/><path d="M5.5 7.5 11 11.5l5.5-4" fill="none" stroke="var(--icon)" stroke-width="1.2"/></svg>
          <span>lorna@thereedyogastudio.example</span>
        </li>
        <li>
          <svg viewBox="0 0 22 22" aria-hidden="true"><circle cx="11" cy="11" r="11" fill="var(--icon)"/><circle cx="11" cy="11" r="6" fill="none" stroke="#fff" stroke-width="1.3"/><ellipse cx="11" cy="11" rx="2.6" ry="6" fill="none" stroke="#fff" stroke-width="1.1"/><path d="M5 11h12" stroke="#fff" stroke-width="1.1"/></svg>
          <span>www.TheReedYogaStudio.example</span>
        </li>
      </ul>
    </div>
  </section>
</main>
</body>
</html>
```